Logo needed for business card

Velquist Pty Ltd is in the business of healthcare and ecommerce.

We own and manage pharmacies and online health ecomerce sites.

We provide ecommerce consultants for companies looking for an ecommerce business startegy.

Think of it as the umbrella under which several healthcare brands may sit.

When I think of Velquist, I visulaise slick black/metalic colours, so please stay away from the common blue and green colours that seem to be so popular in this field.

Target Market(s)

CEOs and COOs

Industry/Entity Type

Healthcare

Contact Information for Business Card

Tessa Lindqvist
Director
Velquist Pty Ltd
4/362 Fennick Pde
Brellton, NSW 2148

Requirements
Must have
• Design must have scope to be implemented on the company's website and letterheads etc.

```html
<!DOCTYPE html>
<html lang="en">
<head>
<meta charset="utf-8">
<title>Velquist Pty Ltd — Business Card</title>
<link href="https://fonts.googleapis.com/css2?family=Arimo:wght@400;700&display=swap" rel="stylesheet">
<style>
  :root {
    --backdrop: #2a2a2c;
    --card-light: #efefef;
    --card-dark: #0a0a0a;
    --gold: #d2a548;
    --ink: #3a3a3a;
    --ink-soft: #5a5a5a;
  }
  * { margin: 0; padding: 0; box-sizing: border-box; }
  html, body {
    width: 1200px; height: 900px; overflow: hidden;
    background: var(--backdrop);
    font-family: "Arimo", Arial, sans-serif;
  }
  .stage { position: relative; width: 1200px; height: 900px; }
  .card {
    position: absolute;
    width: 525px; height: 300px;
    box-shadow: 0 10px 30px rgba(0,0,0,.45);
  }
  .card--front { left: 80px; top: 110px; background: var(--card-light); }
  .card--back  { left: 595px; top: 490px; background: var(--card-dark); }

  .wordmark {
    position: absolute;
    display: flex; align-items: center; gap: 12px;
    color: var(--gold); font-weight: 700; white-space: nowrap;
  }
  .wordmark__dot { border-radius: 50%; background: var(--gold); flex: none; }
  .card--front .wordmark { left: 140px; top: 52px; font-size: 27px; }
  .card--front .wordmark__dot { width: 26px; height: 26px; }
  .card--back .wordmark {
    left: 50%; top: 50%; transform: translate(-50%, -50%);
    font-size: 44px;
  }
  .card--back .wordmark__dot { width: 40px; height: 40px; }

  .person { position: absolute; right: 40px; top: 128px; text-align: right; }
  .person__name { color: var(--gold); font-weight: 700; font-size: 22px; }
  .person__role { color: var(--ink); font-size: 11px; margin-top: 3px; }

  .contact {
    position: absolute; left: 36px; bottom: 30px;
    color: var(--ink); font-size: 13px; line-height: 1.3;
  }
  .contact__address { margin-bottom: 10px; }
  .contact__label { color: var(--gold); margin-right: 4px; }
  .contact__web { color: var(--gold); }
</style>
</head>
<body>
  <main class="stage">
    <section class="card card--front">
      <div class="wordmark">
        <span class="wordmark__dot"></span>
        <span class="wordmark__name">Velquist Pty Ltd</span>
      </div>

      <div class="person">
        <p class="person__name">Tessa Lindqvist</p>
        <p class="person__role">Director</p>
      </div>

      <div class="contact">
        <p class="contact__address">Velquist Pty Ltd<br>4/362 Fennick Pde Brellton, NSW 2148</p>
        <p><span class="contact__label">P</span>+ (0) 123 456 8879</p>
        <p><span class="contact__label">E</span>TLindqvist@youremailaddress.com</p>
        <p class="contact__web">www.yourwebaddress.com</p>
      </div>
    </section>

    <section class="card card--back">
      <div class="wordmark">
        <span class="wordmark__dot"></span>
        <span class="wordmark__name">Velquist Pty Ltd</span>
      </div>
    </section>
  </main>
</body>
</html>
```